Brightmoor Card Company Business Cards

We are a trading card store with Zorblix, sports and other TCG cards, we need a business card design that encompasses a clean cut, modern style with a retro flare. website is brightmoorcardco.com for reference. Can utilize a comic book era feel or a more modern outdoor feel to utilize the "Pacific Northwest" elements of tress, mountains, etc.

Industry/Entity Type

Trading cards and collectibles

Contact Information for Business Card

business name, email address, phone number, name, owner job title

Font styles to use
Sans Serif

```html
<!DOCTYPE html>
<html lang="en">
<head>
<meta charset="utf-8">
<title>Brightmoor Card Company – Business Cards</title>
<link rel="stylesheet" href="https://fonts.googleapis.com/css2?family=Jost:wght@500;700&family=Nunito:wght@400;500&display=swap">
<style>
  :root {
    --backdrop: #d2d3d5;
    --card: #ffffff;
    --brand-grey: #717171;
    --brand-cyan: #12bfe0;
    --ink: #2e2e2e;
  }
  * { margin: 0; padding: 0; box-sizing: border-box; }
  html, body { width: 900px; height: 1200px; overflow: hidden; }
  body { background: var(--backdrop); position: relative; font-family: "Nunito", sans-serif; color: var(--ink); }

  .card {
    position: absolute;
    left: 135px;
    width: 631px;
    background: var(--card);
    border-radius: 14px;
  }
  .card--front { top: 215px; height: 357px; }
  .card--back  { top: 628px; height: 359px; }

  .wordmark {
    position: absolute;
    display: flex;
    flex-direction: column;
    align-items: center;
    justify-content: center;
    gap: 14px;
    text-align: center;
  }
  .wordmark__dot {
    width: 22px; height: 22px; border-radius: 50%;
    background: var(--brand-cyan);
  }
  .wordmark__name {
    font-family: "Jost", sans-serif;
    font-weight: 700;
    color: var(--brand-grey);
    text-transform: uppercase;
    letter-spacing: 2px;
    line-height: 1.15;
  }
  .card--front .wordmark { left: 165px; top: 50px; width: 300px; height: 256px; }
  .card--front .wordmark__name { font-size: 30px; }
  .card--back .wordmark { left: 405px; top: 26px; width: 196px; height: 170px; gap: 10px; }
  .card--back .wordmark__dot { width: 16px; height: 16px; }
  .card--back .wordmark__name { font-size: 20px; letter-spacing: 1.5px; }

  .contact { position: absolute; left: 36px; top: 198px; }
  .contact__name {
    font-family: "Jost", sans-serif;
    font-weight: 700;
    font-size: 25px;
    color: var(--brand-cyan);
    letter-spacing: 0.3px;
    line-height: 1;
  }
  .contact__title { font-size: 14.5px; margin-top: 7px; letter-spacing: 0.6px; }
  .contact__rule { width: 43px; height: 2px; background: var(--brand-cyan); margin-top: 4px; }
  .contact__list { list-style: none; margin-top: 12px; }
  .contact__item {
    display: flex; align-items: center; gap: 6px;
    font-size: 14.5px; letter-spacing: 0.6px; height: 25px;
  }
  .contact__item--phone { letter-spacing: 2.4px; }
  .contact__icon { width: 15px; height: 15px; flex: none; fill: var(--brand-cyan); }
</style>
</head>
<body>

<section class="card card--front" aria-label="Business card front">
  <div class="wordmark">
    <span class="wordmark__dot"></span>
    <span class="wordmark__name">Brightmoor<br>Card Company</span>
  </div>
</section>

<section class="card card--back" aria-label="Business card back">
  <div class="wordmark">
    <span class="wordmark__dot"></span>
    <span class="wordmark__name">Brightmoor<br>Card Company</span>
  </div>

  <div class="contact">
    <h1 class="contact__name">DALTON REYES</h1>
    <p class="contact__title">Owner</p>
    <div class="contact__rule"></div>
    <ul class="contact__list">
      <li class="contact__item contact__item--phone">
        <svg class="contact__icon" viewBox="0 0 24 24" aria-hidden="true"><path d="M6.6 10.8a15 15 0 0 0 6.6 6.6l2.2-2.2c.3-.3.7-.4 1-.2 1.1.4 2.3.6 3.6.6.6 0 1 .4 1 1V20c0 .6-.4 1-1 1A17 17 0 0 1 3 4c0-.6.4-1 1-1h3.5c.6 0 1 .4 1 1 0 1.3.2 2.5.6 3.6.1.3 0 .7-.2 1z"/></svg>
        1 (555) 014-2290
      </li>
      <li class="contact__item">
        <svg class="contact__icon" viewBox="0 0 24 24" aria-hidden="true"><path d="M2 5h20v14H2z M3.5 6.5 12 13l8.5-6.5v-.1h-17z" fill-rule="evenodd"/><path d="M2 5l10 8 10-8v1.8l-10 8-10-8z" fill="#fff"/></svg>
        info@brightmoorcardco.com
      </li>
      <li class="contact__item">
        <svg class="contact__icon" viewBox="0 0 24 24" aria-hidden="true"><path d="M12 2a10 10 0 1 0 0 20 10 10 0 0 0 0-20zm6.9 6h-2.9a15 15 0 0 0-1.4-3.6A8 8 0 0 1 18.9 8zM12 4c.8 1.2 1.5 2.5 1.9 4h-3.8c.4-1.5 1.1-2.8 1.9-4zM4.3 14a8 8 0 0 1 0-4h3.3a16 16 0 0 0 0 4zm.8 2h2.9c.3 1.3.8 2.5 1.4 3.6A8 8 0 0 1 5.1 16zM8 8H5.1a8 8 0 0 1 4.3-3.6C8.8 5.5 8.3 6.7 8 8zm4 12c-.8-1.2-1.5-2.5-1.9-4h3.8c-.4 1.5-1.1 2.8-1.9 4zm2.3-6H9.7a14 14 0 0 1 0-4h4.6a14 14 0 0 1 0 4zm.3 5.6c.6-1.1 1.1-2.3 1.4-3.6h2.9a8 8 0 0 1-4.3 3.6zm1.8-5.6a16 16 0 0 0 0-4h3.3a8 8 0 0 1 0 4z"/></svg>
        brightmoorcardco.com
      </li>
    </ul>
  </div>
</section>

</body>
</html>
```